Website for Law Firm in California with Existing Logo (Pagewright)

I need a website for a law firm based in Orange County, California, called "Hollis Legal Group." The firm will provide civil litigation and business advice services. The principal practice areas include business litigation, real estate litigation, construction litigation, and other general commercial litigation.

I practiced at a very large, international law firm for 10 years (Merrow Tash LLP) before starting Hollis Legal Group.

At the moment, Hollis Legal Group has one attorney, Corwin J. Hollis (me).

I have a logo for Hollis Legal Group (see attached files, including vectors and transparent background)--which is dark blue and gray. I am open to color changes/tweaks, but would prefer designs that communicate dependability, competence, sophistication, and trustworthiness.

The site should include a home page, as well as separate pages containing: (1) information about the firm and Corwin Hollis (e.g., "About"); (2) information about the firm's practice areas (use "Practice Areas"); (3) a "Contact Us" page where the visitor can insert contact information and describe their legal problem or help sought; (4) a page for articles and blog posts.

I'd also like to mention the practice areas on the main page with links to pages dedicated to each practice area. My thought is that these "practice areas" pages will have a similar look and design, but I will, of course, alter the content for each one.

The practice areas to list for now (I may add more or remove some later are):

Business Litigation
Real Estate Litigation
Banking & Lending Litigation
Contract Disputes
Construction Litigation
Commercial Litigation
Fraud Claims
Breach of Fiduciary Claims
Creditor's Rights
Judgment Collection
Appellate Law
Consumer and Personal Injury Claims
ADA Disputes
Other Civil Litigation
General Corporate Advice
Contract Review
Business Entity Formation

Each page should include easily viewable contact information without appearing cheesy.

I uploaded some head shots and photos of my building as well. They need not all be used. Feel free to play with adjustments to the photos (B&W, contrast, etc.).

I own and reserve the copyright to all files, logos, and pictures uploaded with this design.

I will provide a description of the firm and Corwin Hollis for the about page, as well as a summary of each practice area for the practice area page.

I will also need the ability to put a small description of the localities served by the firm at the bottom of each page on the site, along with a website disclaimer about representations made (I will provide the language for this too).

I am contemplating creating additional websites for different practice areas as well. So this may grow into a larger project if your design is selected. I will likely want to link to those sites from my home site if it makes sense to do so.

Thank you.

Reason: I was involved in a car incident yesterday and need a few more days to review designs. Thanks.

Target Market(s)

Legal Services for businesses and business owners, also individuals.

Industry/Entity Type

Attorney

Contact Information for Business Card

Please include my name and the title "Managing Attorney." Please include fields for my address, telephone number, and email address. Also please include "Orange County" and "Los Angeles" on the card.

Font styles to use
Sans Serif

Requirements
Must have
• See description
Nice to have
• See description
Should not have
• See description

```html
<!DOCTYPE html>
<html lang="en">
<head>
<meta charset="utf-8">
<title>Hollis Legal Group</title>
<link rel="stylesheet" href="https://fonts.googleapis.com/css2?family=Playfair+Display:wght@400;700&family=Lato:wght@400;700&display=swap">
<style>
:root{
  --navy:#1c2f7a;
  --blue-deep:#1d3585;
  --blue-mid:#2650b3;
  --blue-light:#3f74d8;
  --ink:#2b2b2b;
  --grey-text:#8a8a8a;
  --grey-light:#f2f2f2;
  --line:#e2e2e2;
  --dark:#333333;
  --white:#ffffff;
  --gold:#e8b33a;
}
*{box-sizing:border-box;margin:0;padding:0}
html,body{width:1200px;height:5114px;overflow:hidden;background:var(--white)}
body{position:relative;font-family:'Lato',sans-serif;color:var(--ink)}
.abs{position:absolute}
.photo{position:absolute}

/* header */
.topbar{position:absolute;left:0;top:0;width:1200px;height:104px}
.topbar .phone{left:41px;top:32px}
.label{font-size:10px;letter-spacing:2px;text-transform:uppercase;color:var(--grey-text)}
.topbar .phone .num{font-family:'Playfair Display',serif;font-size:20px;color:var(--navy);margin-top:4px}
.brand{position:absolute;left:0;width:1200px;top:24px;text-align:center;font-family:'Playfair Display',serif;font-size:40px;color:var(--navy);letter-spacing:3px;font-weight:400}
.book{right:41px;top:26px;width:170px;height:46px;border:1px solid var(--line);border-radius:23px;text-align:center;padding-top:6px}
.book .big{font-family:'Playfair Display',serif;font-size:17px;color:var(--navy);letter-spacing:1px}
.nav{position:absolute;top:112px;left:0;width:1200px;text-align:center;font-size:10px;letter-spacing:2px;text-transform:uppercase;color:var(--ink)}
.nav span{margin:0 34px}
.nav-line{position:absolute;top:133px;left:41px;width:1125px;height:1px;background:var(--line)}

/* hero */
.hero{left:41px;top:144px;width:1125px;height:638px;overflow:hidden}
.hero-blue{left:0;top:0;width:600px;height:638px;background:var(--blue-deep)}
.hero-photo{left:566px;top:0;width:559px;height:638px;
  background:
    linear-gradient(180deg,rgba(0,0,0,0) 55%,rgba(20,24,36,.85) 82%,#151a28 100%),
    radial-gradient(ellipse 42% 48% at 46% 40%,#b48c78 0%,#9c7a68 45%,rgba(156,122,104,0) 100%),
    linear-gradient(100deg,#d7dade 0%,#c3c7cc 30%,#8f959e 65%,#4d535e 100%)}
.hero h1{left:194px;top:80px;font-family:'Playfair Display',serif;font-size:60px;line-height:60px;color:var(--white);font-weight:400}
.hero .who{left:194px;top:300px;font-size:15px;font-weight:700;color:var(--white)}
.dots{left:92px;top:230px;width:6px}
.dots i{display:block;width:6px;height:6px;border-radius:3px;background:var(--white);margin-bottom:10px;opacity:.6}
.dots i:first-child{opacity:1}
.btn-dark{position:absolute;background:var(--dark);color:var(--white);font-size:10px;letter-spacing:2px;text-transform:uppercase;text-align:center;font-weight:700}
.hero .btn-dark{left:194px;top:356px;width:176px;height:50px;line-height:50px}

/* service cards */
.cards{left:233px;top:651px;width:737px;height:491px;display:flex}
.card{position:relative;width:33.333%;height:491px}
.card .pic{position:absolute;left:0;top:0;width:100%;height:247px}
.card:nth-child(1) .pic{background:
  radial-gradient(ellipse 60% 40% at 50% 55%,#f0f0f0 0%,rgba(240,240,240,0) 100%),
  linear-gradient(160deg,#bdbdbd 0%,#8e8e8e 50%,#4a4a4a 100%)}
.card:nth-child(2) .pic{background:
  radial-gradient(ellipse 55% 35% at 50% 45%,#7a7a7a 0%,rgba(122,122,122,0) 100%),
  linear-gradient(160deg,#565656 0%,#2c2c2c 60%,#111 100%)}
.card:nth-child(3) .pic{background:
  radial-gradient(ellipse 50% 40% at 62% 35%,#fafafa 0%,rgba(250,250,250,0) 100%),
  linear-gradient(160deg,#dedede 0%,#a8a8a8 55%,#5e5e5e 100%)}
.card .body{position:absolute;left:0;top:247px;width:100%;height:244px;text-align:center;color:var(--white);padding:52px 22px 0}
.card:nth-child(1) .body{background:var(--blue-deep)}
.card:nth-child(2) .body{background:var(--blue-mid)}
.card:nth-child(3) .body{background:var(--blue-light)}
.card .plus{position:absolute;left:50%;top:225px;margin-left:-22px;width:44px;height:44px;border-radius:22px;background:var(--white);z-index:2;text-align:center;line-height:42px;font-size:22px;color:var(--blue-mid)}
.card h3{font-family:'Playfair Display',serif;font-size:21px;line-height:24px;font-weight:400;height:52px;display:flex;align-items:center;justify-content:center}
.card p{font-size:11px;line-height:17px;opacity:.85;margin-top:10px}
.card .more{font-size:9px;letter-spacing:2px;font-weight:700;margin-top:18px}

/* call now */
.callnow{left:0;top:1210px;width:1200px;text-align:center}
.callnow .kick{font-family:'Playfair Display',serif;font-size:16px;color:var(--navy);letter-spacing:1px}
.callnow .big{font-family:'Playfair Display',serif;font-size:42px;color:var(--navy);letter-spacing:1px;margin-top:2px;font-weight:700}
.callnow p{width:800px;margin:14px auto 0;font-size:13px;line-height:20px;color:var(--grey-text)}

/* feature banner */
.banner1{left:41px;top:1440px;width:1125px;height:446px;background:
  radial-gradient(ellipse 22% 45% at 72% 55%,#c9cdd1 0%,rgba(201,205,209,0) 100%),
  linear-gradient(180deg,rgba(40,60,90,0) 60%,rgba(35,58,48,.7) 100%),
  linear-gradient(90deg,#28436b 0%,#3e5a80 35%,#6f8299 60%,#8d98a4 75%,#3d4b5c 100%)}
.frame{position:absolute;border:1px solid rgba(255,255,255,.7)}
.banner1 .frame{left:16px;top:16px;width:1093px;height:414px}
.features{left:240px;top:1508px}
.feature{position:relative;height:110px;padding-left:62px;color:var(--white)}
.feature .ico{position:absolute;left:0;top:0;width:40px;height:40px;border-radius:20px;background:var(--blue-light);display:flex;align-items:center;justify-content:center}
.feature h4{font-family:'Playfair Display',serif;font-size:19px;font-weight:400;line-height:26px}
.feature p{font-size:11px;line-height:17px;opacity:.85;width:300px;margin-top:4px}

/* practice areas */
.section-head{position:absolute;left:0;width:1200px;text-align:center}
.section-head .kick{font-family:'Playfair Display',serif;font-size:14px;color:var(--navy);letter-spacing:2px;text-transform:uppercase}
.section-head h2{font-family:'Playfair Display',serif;font-size:36px;color:var(--navy);font-weight:400;letter-spacing:1px;text-transform:uppercase;margin-top:2px}
.areas{left:232px;top:2072px;width:740px;display:grid;grid-template-columns:repeat(3,1fr);row-gap:30px;column-gap:30px}
.area{text-align:center}
.area .ico{width:34px;height:34px;border-radius:17px;margin:0 auto;display:flex;align-items:center;justify-content:center}
.area .ico.on{background:var(--navy)}
.area h5{font-family:'Playfair Display',serif;font-size:15px;color:var(--navy);font-weight:400;margin-top:12px}
.area .rule{width:60px;height:1px;background:var(--line);margin:8px auto}
.area p{font-size:11px;line-height:16px;color:var(--grey-text)}
.arrow{position:absolute;top:2180px}

/* appointment */
.appt-photo{left:41px;top:2428px;width:576px;height:542px;background:
  radial-gradient(circle at 30% 12%,#ffffff 0%,#e8f0fb 12%,rgba(232,240,251,0) 35%),
  linear-gradient(180deg,rgba(0,0,0,0) 70%,rgba(16,34,28,.75) 100%),
  linear-gradient(200deg,#cfe0f6 0%,#6f93cb 35%,#2b4f8f 70%,#1d2f52 100%)}
.appt{left:617px;top:2428px;width:549px;height:542px;background:var(--grey-light);padding:78px 62px 0}
.appt .kick{font-family:'Playfair Display',serif;font-size:15px;color:var(--navy);letter-spacing:2px;text-transform:uppercase}
.appt h2{font-family:'Playfair Display',serif;font-size:34px;color:var(--navy);font-weight:400;text-transform:uppercase;margin-top:2px}
.field{width:410px;height:36px;background:var(--white);margin-top:14px;font-size:10px;color:#b5b5b5;letter-spacing:1px;padding:12px 14px}
.field:first-of-type{margin-top:22px}
.field.area-txt{height:112px}
.appt .btn-dark{position:relative;display:block;width:168px;height:48px;line-height:48px;margin-top:38px}

/* feedbacks */
.fb-text{left:138px;top:3050px;width:240px}
.fb-text .kick{font-family:'Playfair Display',serif;font-size:14px;color:var(--navy);letter-spacing:1px;text-transform:uppercase}
.fb-text h2{font-family:'Playfair Display',serif;font-size:34px;color:var(--navy);font-weight:400;text-transform:uppercase}
.fb-text p{font-size:12px;line-height:19px;color:var(--grey-text);margin-top:10px}
.stars{margin-top:14px;color:var(--gold);font-size:13px;letter-spacing:2px}
.fb-photo{left:498px;top:3050px;width:230px;height:230px;border-radius:115px;background:
  linear-gradient(180deg,rgba(0,0,0,0) 55%,#1d2436 72%,#161b2a 100%),
  radial-gradient(ellipse 30% 34% at 50% 40%,#c79e86 0%,rgba(199,158,134,0) 100%),
  linear-gradient(180deg,#e3e6ea 0%,#b9bfc8 100%);box-shadow:0 0 0 6px var(--white),0 6px 20px rgba(0,0,0,.18)}
.quote-mark{left:742px;top:3050px;font-family:'Playfair Display',serif;font-size:52px;color:var(--navy);line-height:52px}
.fb-quote{left:776px;top:3065px;width:260px;font-size:12px;line-height:18px;color:var(--grey-text)}
.fb-quote .who{font-size:9px;letter-spacing:2px;color:var(--blue-light);margin-top:12px;text-transform:uppercase}
.avatar{position:absolute;top:3344px;width:72px;height:72px;border-radius:36px;background:
  linear-gradient(180deg,rgba(0,0,0,0) 58%,#3a4254 75%,#2b3242 100%),
  radial-gradient(ellipse 32% 36% at 50% 42%,#cda48c 0%,rgba(205,164,140,0) 100%),
  linear-gradient(180deg,#e6e8eb,#b3b9c2)}

/* second banner */
.banner2{left:41px;top:3474px;width:1125px;height:374px;background:
  linear-gradient(180deg,rgba(0,0,0,0) 65%,rgba(12,30,30,.6) 100%),
  linear-gradient(90deg,#22386a 0%,#3e5f98 30%,#5a7ab0 55%,#3a5a93 75%,#1e3565 100%)}
.banner2 .inner{position:absolute;left:0;top:78px;width:1125px;text-align:center;color:var(--white)}
.banner2 .kick{font-family:'Playfair Display',serif;font-size:14px;letter-spacing:2px;text-transform:uppercase;margin-top:10px}
.banner2 h2{font-family:'Playfair Display',serif;font-size:40px;font-weight:400;color:#c8d6f0;text-transform:uppercase;letter-spacing:1px}
.banner2 .pill{width:230px;height:30px;background:var(--white);margin:14px auto 0;font-size:9px;letter-spacing:2px;color:#999;line-height:30px}
.banner2 .circ{width:34px;height:34px;border-radius:17px;background:rgba(255,255,255,.3);margin:22px auto 0}

/* blog */
.posts{left:233px;top:3988px;width:764px;display:flex;justify-content:space-between}
.post{width:245px;height:378px;background:var(--white);box-shadow:0 2px 10px rgba(0,0,0,.08);text-align:center}
.post .pic{height:158px}
.post:nth-child(1) .pic{background:
  linear-gradient(180deg,rgba(0,0,0,0) 55%,#2f3a52 78%,#26304a 100%),
  radial-gradient(ellipse 22% 26% at 50% 34%,#caa088 0%,rgba(202,160,136,0) 100%),
  linear-gradient(90deg,#8a7450 0%,#d2c29c 30%,#e4d8b8 50%,#cbb78e 70%,#7c6744 100%)}
.post:nth-child(2) .pic{background:
  radial-gradient(circle at 25% 10%,#ffffff 0%,rgba(255,255,255,0) 30%),
  linear-gradient(200deg,#e9f0fa,#4b7ac1 55%,#1f3f78)}
.post:nth-child(3) .pic{background:
  linear-gradient(180deg,rgba(0,0,0,0) 55%,#262d40 78%,#1c2233 100%),
  radial-gradient(ellipse 22% 26% at 50% 34%,#c89d86 0%,rgba(200,157,134,0) 100%),
  linear-gradient(90deg,#4f5a68 0%,#9aa5b3 35%,#b8c1cc 50%,#8d98a6 70%,#3e4a5c 100%)}
.post .date{font-size:9px;letter-spacing:2px;color:var(--grey-text);margin-top:22px}
.post h4{font-family:'Playfair Display',serif;font-size:15px;line-height:19px;color:var(--ink);font-weight:700;margin:6px 26px 0}
.post p{font-size:11px;line-height:16px;color:var(--grey-text);margin:12px 24px 0}
.post .more{font-size:9px;letter-spacing:2px;color:var(--navy);font-weight:700;margin-top:16px}

/* contact blocks */
.info{left:41px;top:4414px;width:1125px;height:286px;display:flex}
.info .col{flex:1;text-align:center;color:var(--white);padding-top:66px}
.info .col:nth-child(1){background:var(--blue-deep)}
.info .col:nth-child(2){background:var(--blue-mid)}
.info .col:nth-child(3){background:var(--blue-light)}
.info .ico{width:44px;height:44px;border-radius:22px;background:var(--white);margin:0 auto;display:flex;align-items:center;justify-content:center}
.info h4{font-family:'Playfair Display',serif;font-size:22px;font-weight:400;margin-top:14px}
.info p{font-size:10px;letter-spacing:2px;line-height:17px;margin-top:10px;text-transform:uppercase}

/* footer */
.footer{left:41px;top:4700px;width:1125px;height:359px;background:var(--dark);color:var(--white)}
.footer .links{position:absolute;left:68px;top:74px}
.footer .links h5{font-family:'Playfair Display',serif;font-size:16px;font-weight:400;text-transform:uppercase;letter-spacing:1px}
.footer .links li{list-style:none;font-size:11px;color:#b9b9b9;border-bottom:1px solid #4a4a4a;padding:6px 0;width:200px}
.footer .links ul{margin-top:16px}
.footer .fbrand{position:absolute;left:0;top:36px;width:1125px;text-align:center;font-family:'Playfair Display',serif;font-size:34px;letter-spacing:3px}
.footer .about{position:absolute;left:412px;top:118px;width:300px;text-align:center;font-size:11px;line-height:18px;color:#b9b9b9}
.socials{position:absolute;left:0;top:296px;width:1125px;display:flex;justify-content:center;gap:6px}
.socials i{display:block;width:18px;height:18px;border-radius:9px;background:var(--blue-light)}
.socials i:nth-child(3){background:#3b8be0}
.socials i:nth-child(4){background:#d6463b}
.socials i:nth-child(5){background:#c6302b}
.copy{position:absolute;left:0;top:5080px;width:1200px;text-align:center;font-size:9px;letter-spacing:2px;color:var(--grey-text);text-transform:uppercase}
</style>
</head>
<body>

<header class="topbar">
  <div class="abs phone"><div class="label">Call today</div><div class="num">800 000 00 00</div></div>
  <div class="brand">HOLLIS LEGAL GROUP</div>
  <div class="abs book"><div class="label">Make booking</div><div class="big">APPOINTMENT</div></div>
</header>
<nav class="nav"><span>Homepage</span><span>About us</span><span>Practice areas</span><span>Our blog</span><span>Contacts</span></nav>
<div class="nav-line"></div>

<section class="abs hero">
  <div class="abs hero-blue"></div>
  <div class="photo hero-photo" role="img" aria-label="Portrait of attorney Corwin J. Hollis in a dark suit"></div>
  <div class="abs dots"><i></i><i></i><i></i></div>
  <h1 class="abs">Every<br>Client<br>Matters</h1>
  <div class="abs who">Corwin J. Hollis</div>
  <div class="btn-dark">Request a consult</div>
</section>

<section class="abs cards">
  <article class="card">
    <div class="pic" role="img" aria-label="Black and white photo of a business handshake"></div>
    <div class="plus">+</div>
    <div class="body"><h3>business Litigation</h3><p>Sharp counsel for owners facing partner, vendor and contract fights in court.</p><div class="more">READ MORE</div></div>
  </article>
  <article class="card">
    <div class="pic" role="img" aria-label="Black and white photo of a gavel beside a small house model"></div>
    <div class="plus">+</div>
    <div class="body"><h3>Real<br>Estate Litigation</h3><p>Title, lease and purchase disputes handled with care from start to end.</p><div class="more">READ MORE</div></div>
  </article>
  <article class="card">
    <div class="pic" role="img" aria-label="Black and white photo of a hard hat next to a gavel"></div>
    <div class="plus">+</div>
    <div class="body"><h3>Construction<br>Litigation</h3><p>Defect, lien and payment claims for builders, owners and contractors.</p><div class="more">READ MORE</div></div>
  </article>
</section>

<section class="abs callnow">
  <div class="kick">HAVE ANY PROBLEMS BUT CAN'T CONSULT TO ANYONE?</div>
  <div class="big">CALL NOW: 800 000 00 00</div>
  <p>Speak directly with an attorney about your matter. We listen first, explain your options in plain words, and give an honest view of the path ahead before any work begins on your case.</p>
</section>

<section class="abs banner1" role="img" aria-label="Office courtyard with palm trees and a statue of Lady Justice">
  <div class="frame"></div>
</section>
<div class="abs features">
  <div class="feature"><div class="ico"><svg width="16" height="16"><rect x="2" y="2" width="12" height="12" fill="none" stroke="#fff" stroke-width="1.5"/><path d="M5 6h6M5 9h6M5 12h4" stroke="#fff" stroke-width="1.2"/></svg></div><h4>Detailed Planning</h4><p>Every case starts with a clear plan built around your goals and budget.</p></div>
  <div class="feature"><div class="ico"><svg width="16" height="16"><path d="M2 8l4 4 8-8" fill="none" stroke="#fff" stroke-width="2"/></svg></div><h4>Settlement</h4><p>We pursue fair resolution early when it truly serves your interests.</p></div>
  <div class="feature"><div class="ico"><svg width="16" height="16"><path d="M8 1 2 4v4c0 3 3 6 6 7 3-1 6-4 6-7V4z" fill="#fff"/></svg></div><h4>Fight for Justice</h4><p>When trial is needed, we prepare fully and argue with conviction.</p></div>
</div>

<div class="section-head" style="top:1962px"><div class="kick">Legal</div><h2>Practice Areas</h2></div>
<svg class="arrow" style="left:112px" width="14" height="24" viewBox="0 0 14 24"><path d="M12 2 2 12l10 10" fill="none" stroke="#1c2f7a" stroke-width="2.5"/></svg>
<svg class="arrow" style="left:1074px" width="14" height="24" viewBox="0 0 14 24"><path d="M2 2l10 10L2 22" fill="none" stroke="#1c2f7a" stroke-width="2.5"/></svg>
<section class="abs areas">
  <div class="area"><div class="ico"><svg width="16" height="14"><rect x="1" y="4" width="14" height="9" fill="#1c2f7a"/><rect x="5" y="1" width="6" height="4" fill="none" stroke="#1c2f7a" stroke-width="1.5"/></svg></div><h5>Business Litigation</h5><div class="rule"></div><p>Company disputes resolved with focus<br>and a steady, proven hand.</p></div>
  <div class="area"><div class="ico on"><svg width="16" height="14"><path d="M8 1 1 7h2v6h10V7h2z" fill="#fff"/></svg></div><h5>Real Estate Litigation</h5><div class="rule"></div><p>Property, lease and title claims for<br>owners, buyers and lenders.</p></div>
  <div class="area"><div class="ico"><svg width="16" height="14"><path d="M8 1 1 5h14z" fill="#1c2f7a"/><rect x="2" y="6" width="2" height="5" fill="#1c2f7a"/><rect x="7" y="6" width="2" height="5" fill="#1c2f7a"/><rect x="12" y="6" width="2" height="5" fill="#1c2f7a"/><rect x="1" y="12" width="14" height="2" fill="#1c2f7a"/></svg></div><h5>Banking &amp; Lending Litigation</h5><div class="rule"></div><p>Loan, guaranty and lender claims<br>handled with precision.</p></div>
  <div class="area"><div class="ico"><svg width="12" height="16"><rect x="1" y="1" width="10" height="14" fill="#1c2f7a"/><rect x="3" y="3" width="2" height="2" fill="#fff"/><rect x="7" y="3" width="2" height="2" fill="#fff"/><rect x="3" y="7" width="2" height="2" fill="#fff"/><rect x="7" y="7" width="2" height="2" fill="#fff"/></svg></div><h5>Construction Litigation</h5><div class="rule"></div><p>Defect, delay and lien matters for<br>every party on the job.</p></div>
  <div class="area"><div class="ico"><svg width="16" height="12"><rect x="1" y="1" width="14" height="10" fill="none" stroke="#1c2f7a" stroke-width="1.5"/><path d="M1 1l7 6 7-6" fill="none" stroke="#1c2f7a" stroke-width="1.5"/></svg></div><h5>Commercial Litigation</h5><div class="rule"></div><p>Trade and contract disputes argued<br>with clear strategy.</p></div>
  <div class="area"><div class="ico"><svg width="14" height="16"><path d="M7 1 2 3v5c0 3 2 6 5 7 3-1 5-4 5-7V3z" fill="#1c2f7a"/></svg></div><h5>Judgment Collection</h5><div class="rule"></div><p>We turn court awards into recovered<br>funds for our clients.</p></div>
</section>

<div class="photo appt-photo" role="img" aria-label="Glass office tower against a bright sunny sky with palm trees"></div>
<section class="abs appt">
  <div class="kick">Don't hesitate to</div>
  <h2>Make Appointment</h2>
  <div class="field">✓ YOUR NAME</div>
  <div class="field">✉ EMAIL ADDRESS</div>
  <div class="field area-txt">✎ MESSAGE</div>
  <div class="btn-dark">Request a consult</div>
</section>

<section class="abs fb-text">
  <div class="kick">My client's</div>
  <h2>Feedbacks</h2>
  <p>Kind words from the owners and families we have stood beside in court and at the table.</p>
  <div class="stars">★★★★★</div>
</section>
<div class="photo fb-photo" role="img" aria-label="Round portrait of a client in a dark suit"></div>
<div class="abs quote-mark">“</div>
<div class="abs fb-quote">Calm, clear and always prepared. He explained every step and won a result that kept my business running strong.<div class="who">Client, business owner</div></div>
<div class="avatar" style="left:484px" role="img" aria-label="Client portrait"></div>
<div class="avatar" style="left:566px" role="img" aria-label="Client portrait"></div>
<div class="avatar" style="left:648px" role="img" aria-label="Client portrait"></div>

<section class="abs banner2" role="img" aria-label="Blue toned office building with palm trees">
  <div class="inner">
    <svg width="18" height="20"><circle cx="9" cy="5" r="4" fill="#fff"/><path d="M1 19c0-5 4-8 8-8s8 3 8 8z" fill="#fff"/></svg>
    <div class="kick">Building a better future</div>
    <h2>Common Ground, Uncommon Vision</h2>
    <div class="pill">LEARN MORE</div>
    <div class="circ"></div>
  </div>
</section>

<div class="section-head" style="top:3900px"><div class="kick">Latest news</div><h2>Blog Posts</h2></div>
<section class="abs posts">
  <article class="post"><div class="pic" role="img" aria-label="Attorney standing in an office lobby"></div><div class="date">MARCH 12</div><h4>Lorem ipsum dolor sit consectetur</h4><p>Three steps every owner should take before a contract dispute reaches court.</p><div class="more">READ MORE</div></article>
  <article class="post"><div class="pic" role="img" aria-label="Glass office tower from below"></div><div class="date">MARCH 04</div><h4>Adipiscing elit sedds eiusmod tempor</h4><p>How lien deadlines shape your options on a stalled construction project.</p><div class="more">READ MORE</div></article>
  <article class="post"><div class="pic" role="img" aria-label="Attorney in suit outside the office"></div><div class="date">FEBRUARY 21</div><h4>Incididunt labore et dolore magna</h4><p>What to expect in the first meeting and which papers to bring along.</p><div class="more">READ MORE</div></article>
</section>

<section class="abs info">
  <div class="col"><div class="ico"><svg width="14" height="18"><path d="M7 1a6 6 0 0 0-6 6c0 4 6 10 6 10s6-6 6-10a6 6 0 0 0-6-6z" fill="#1d3585"/><circle cx="7" cy="7" r="2" fill="#fff"/></svg></div><h4>Address</h4><p>1200 Harbor View Drive<br>Orange County, CA</p></div>
  <div class="col"><div class="ico"><svg width="16" height="16"><path d="M3 1l3 3-2 2c1 2 4 5 6 6l2-2 3 3-2 2C7 15 1 9 1 3z" fill="#2650b3"/></svg></div><h4>Contact</h4><p>Phone: 800 000 00 00<br>Email: info@hollislegal.example</p></div>
  <div class="col"><div class="ico"><svg width="16" height="16"><circle cx="8" cy="8" r="6.5" fill="none" stroke="#3f74d8" stroke-width="1.5"/><path d="M8 4v4l3 2" fill="none" stroke="#3f74d8" stroke-width="1.5"/></svg></div><h4>Hours</h4><p>Mon – Fri: 9:00 – 18:00<br>Saturday: 10:00 – 14:00</p></div>
</section>

<footer class="abs footer">
  <div class="links"><h5>Practice Areas</h5><ul><li>Business Litigation</li><li>Real Estate Litigation</li><li>Banking &amp; Lending Litigation</li><li>Contract Disputes</li></ul></div>
  <div class="fbrand">HOLLIS LEGAL GROUP</div>
  <p class="about">Serving businesses and individuals across Orange County and Los Angeles. Information on this site is general in nature and does not create an attorney client relationship.</p>
  <div class="socials"><i></i><i></i><i></i><i></i><i></i></div>
</footer>
<div class="copy">Copyright 2024 by Hollis Legal Group</div>

</body>
</html>
```